Business Card Design Project

A business card for a new company in Ontario Canada called Sketch for Growth. It is a consulting company which uses Brixel as the medium for facilitation.

The target market is for senior leaders in healthcare and social services.

Industry/Entity Type

Healthcare

Requirements
Must have
• The name Sketch For Growth
Dana Moreheuse RRT, B Ed (AD ed).
Tacticraft Facililitator (R)

Tag Line
Engaging Transforming and Innovative
The attached logo

danamoreheuse@mailnook.com
555-284-9137
Should not have
• Lime green
Times New Roman or Arial font
Do not include Brixel bricks on the card.

```html
<!DOCTYPE html>
<html lang="en">
<head>
<meta charset="utf-8">
<title>Sketch for Growth – Business Card</title>
<link href="https://fonts.googleapis.com/css2?family=Patrick+Hand&display=swap" rel="stylesheet">
<style>
  :root {
    --page-bg: #2a2a2a;
    --card-top: #ffffff;
    --card-bottom: #e9eaec;
    --band-blue: #2aa9e0;
    --band-line: #9fdcf5;
    --accent-purple: #7a2d91;
    --ink: #1f1f1f;
    --mark-blue: #2aa9e0;
  }
  * { box-sizing: border-box; margin: 0; padding: 0; }
  html, body {
    width: 1200px; height: 676px; overflow: hidden;
    background: var(--page-bg);
    font-family: "Patrick Hand", "Comic Sans MS", cursive;
  }
  .card {
    position: absolute; top: 101px;
    width: 270px; height: 474px;
    border-radius: 12px; overflow: hidden;
    background: linear-gradient(180deg, var(--card-top) 0%, var(--card-bottom) 100%);
  }
  .card--front { left: 283px; }
  .card--back { left: 647px; }

  .brand {
    position: absolute; left: 0; right: 0;
    display: flex; flex-direction: column; align-items: center;
  }
  .card--front .brand { top: 70px; }
  .card--back .brand { top: 44px; }
  .brand__dot {
    width: 96px; height: 96px; border-radius: 50%;
    background: var(--mark-blue);
  }
  .card--back .brand__dot { width: 78px; height: 78px; }
  .brand__name {
    margin-top: 26px;
    font-size: 17px; letter-spacing: 0.5px; color: var(--ink);
    text-transform: uppercase;
  }
  .card--front .brand__name { margin-top: 54px; }
  .card--back .brand__name { font-size: 14px; margin-top: 28px; }

  .band {
    position: absolute; left: 0; right: 0;
    background: var(--band-blue);
    border-top: 2px solid var(--band-line);
    box-shadow: 0 6px 0 -3px var(--band-blue);
  }
  .band::after {
    content: ""; position: absolute; left: 0; right: 0; bottom: 6px;
    height: 1px; background: var(--band-line);
  }
  .card--front .band { top: 353px; height: 86px; }
  .card--back .band { top: 246px; height: 193px; }

  .tagline {
    text-align: center; color: var(--accent-purple);
    font-size: 20px; line-height: 25px; padding-top: 14px;
  }

  .contact { text-align: center; color: var(--ink); }
  .contact__company {
    margin-top: 22px; font-size: 23px; color: var(--accent-purple);
    text-transform: uppercase; letter-spacing: 0.5px;
  }
  .contact__person, .contact__role { font-size: 13px; line-height: 20px; }
  .contact__person { margin-top: 2px; }
  .contact__rule {
    width: 210px; height: 1px; margin: 12px auto 8px;
    background: var(--band-line);
  }
  .contact__line { font-size: 18px; line-height: 22px; }
  .contact__line--small { font-size: 14px; }
  .contact__label { color: var(--accent-purple); margin-right: 6px; }
</style>
</head>
<body>
  <section class="card card--front" aria-label="Card front">
    <div class="brand">
      <div class="brand__dot"></div>
      <div class="brand__name">Sketch for Growth</div>
    </div>
    <div class="band">
      <p class="tagline">Engaging Transforming<br>and Innovative</p>
    </div>
  </section>

  <section class="card card--back" aria-label="Card back">
    <div class="brand">
      <div class="brand__dot"></div>
      <div class="brand__name">Sketch for Growth</div>
    </div>
    <div class="band contact">
      <h1 class="contact__company">Sketch for Growth</h1>
      <p class="contact__person">Dana Moreheuse RRT, BA (AD ed).</p>
      <p class="contact__role">Tacticraft Facililitator (R)</p>
      <div class="contact__rule"></div>
      <p class="contact__line"><span class="contact__label">P:</span>555-284-9137</p>
      <p class="contact__line contact__line--small"><span class="contact__label">E:</span>danamoreheuse@mailnook.com</p>
    </div>
  </section>
</body>
</html>
```